A world class design for a " Discount services provider"
Brightfold Savings Network International
A world class design for a " Discount services provider" - Financial Services
Creative Brief
Simple
Kemi ARUBA
Managing Partner
Suite 204, 306 & 118, Corlenne Plaza, Opp. Former Harbour Works Bureau, Tesvara Crescent , Zone 8, Ilumo Abuja - FCT
infokemiaruba@brightfoldmail.example
www.brightfoldsavingsnet.example
The back of the business card should carry my detailed imformation, while the front should carry only the company's designed logo and colour.
Tavolin Tavolin
Dear Designers, Thank you for the wonderful work you have submitted so far. Looking forward to see more beautiful and creative designs though. Great minds!
Dear Designers, Please remember that I also need the following Stationary designs in addtion to the business card design. 1. Letterhead (A4 Size 210mm x 297mm) 2. Envelope (C4 Size 229mmx324mm) 3. Email Signature

```html
<!DOCTYPE html>
<html lang="en">
<head>
<meta charset="utf-8">
<title>Brightfold Savings Network International – Business Card</title>
<link rel="stylesheet" href="https://fonts.googleapis.com/css2?family=Cinzel:wght@500&family=Arimo:wght@400;700&display=swap">
<style>
  :root {
    --stage: #e9ebee;
    --card-white: #f7f7f8;
    --card-shade: #e6e7ea;
    --brand-blue: #1f4fae;
    --blue-light: #3d8fe6;
    --blue-deep: #0f3a9a;
    --swoosh: #0b0d12;
    --ink-white: #ffffff;
  }
  * { box-sizing: border-box; margin: 0; padding: 0; }
  html, body { width: 1200px; height: 820px; overflow: hidden; }
  body {
    background: var(--stage);
    font-family: "Arimo", Arial, sans-serif;
    display: flex;
    flex-direction: column;
    align-items: center;
    justify-content: center;
    gap: 60px;
  }
  .card {
    position: relative;
    width: 560px;
    height: 320px;
    border-radius: 16px;
    overflow: hidden;
    background: linear-gradient(160deg, var(--card-white) 0%, var(--card-shade) 100%);
    box-shadow: 0 8px 22px rgba(0,0,0,0.18);
  }
  .brand {
    position: absolute;
    display: flex;
    align-items: center;
    gap: 12px;
  }
  .brand-dot {
    width: 46px;
    height: 46px;
    border-radius: 50%;
    border: 3px solid var(--brand-blue);
    flex: none;
  }
  .brand-name {
    font-family: "Cinzel", "Times New Roman", serif;
    font-weight: 500;
    color: var(--brand-blue);
    line-height: 1.2;
    letter-spacing: 0.3px;
    white-space: nowrap;
  }
  .card--front .brand { left: 50%; top: 50%; transform: translate(-50%, -50%); }
  .card--front .brand-name { font-size: 19px; }
  .card--back .brand { left: 34px; top: 82px; }
  .card--back .brand-name { font-size: 13.5px; }
  .back-art { position: absolute; inset: 0; }
  .contact {
    position: absolute;
    right: 30px;
    bottom: 20px;
    text-align: right;
    color: var(--ink-white);
  }
  .contact-name { font-size: 22px; font-weight: 700; }
  .contact-title { font-size: 14px; margin-bottom: 14px; }
  .contact-line {
    font-size: 12.5px;
    line-height: 1.45;
    display: flex;
    justify-content: flex-end;
    align-items: center;
    gap: 6px;
  }
  .contact-line svg { width: 11px; height: 11px; flex: none; }
  .contact-gap { height: 8px; }
</style>
</head>
<body>

<section class="card card--front" aria-label="Business card front">
  <div class="brand">
    <span class="brand-dot"></span>
    <span class="brand-name">Brightfold Savings Network<br>International</span>
  </div>
</section>

<section class="card card--back" aria-label="Business card back">
  <svg class="back-art" viewBox="0 0 560 320" preserveAspectRatio="none" aria-hidden="true">
    <defs>
      <linearGradient id="blue-panel" x1="0" y1="0" x2="1" y2="1">
        <stop offset="0" stop-color="var(--blue-light)"/>
        <stop offset="1" stop-color="var(--blue-deep)"/>
      </linearGradient>
    </defs>
    <path d="M372 0 C 352 120, 340 215, 190 255 C 140 268, 80 272, 20 278 L 0 292 L 0 320 L 560 320 L 560 0 Z" fill="var(--swoosh)"/>
    <path d="M388 0 C 370 125, 358 225, 205 268 C 150 282, 85 284, 20 302 L 0 320 L 560 320 L 560 0 Z" fill="url(#blue-panel)"/>
  </svg>

  <div class="brand">
    <span class="brand-dot"></span>
    <span class="brand-name">Brightfold Savings Network<br>International</span>
  </div>

  <div class="contact">
    <p class="contact-name">Dorian Velkamp</p>
    <p class="contact-title">Director General</p>
    <p class="contact-line">Suite # 418, Orrin</p>
    <p class="contact-line">Bldg, NY 40917</p>
    <div class="contact-gap"></div>
    <p class="contact-line">614302.287
      <svg viewBox="0 0 12 12" fill="currentColor"><path d="M2 1h2.5l1 3-1.5 1a6 6 0 0 0 3 3l1-1.5 3 1V10a1 1 0 0 1-1 1A9 9 0 0 1 1 2a1 1 0 0 1 1-1z"/></svg>
    </p>
    <p class="contact-line">412-608-3157
      <svg viewBox="0 0 12 12" fill="currentColor"><rect x="3" y="0.5" width="6" height="11" rx="1.2"/></svg>
    </p>
    <p class="contact-line">dorian@brightfoldmail.example
      <svg viewBox="0 0 12 12" fill="none" stroke="currentColor" stroke-width="1.2"><rect x="1" y="2.5" width="10" height="7"/><path d="M1 2.5l5 4 5-4"/></svg>
    </p>
    <p class="contact-line">www.brightfoldsavingsnet.example
      <svg viewBox="0 0 12 12" fill="none" stroke="currentColor" stroke-width="1.1"><circle cx="6" cy="6" r="5"/><path d="M1 6h10M6 1c2.5 3 2.5 7 0 10M6 1c-2.5 3-2.5 7 0 10"/></svg>
    </p>
  </div>
</section>

</body>
</html>
```